Business Card design which attached logo. Company is called Tallowind Shield and main colours are Orange & Black.

Company specialises in Paint Protection and Detailing for supercars.

Details needed on business card:

Sales

Address: Unit 14, 172 Garrick Road, Wexley Vale, NSW 2381

Phone: 02 9461 2738

website: www.tallowindshield.com.au

Email: sales@tallowindshield.com.au

```html
<!DOCTYPE html>
<html lang="en">
<head>
<meta charset="utf-8">
<title>Tallowind Shield — Business Card</title>
<link href="https://fonts.googleapis.com/css2?family=Arimo:wght@300;400;700&display=swap" rel="stylesheet">
<style>
  :root {
    --orange: #ee5a24;
    --black: #1f1c1a;
    --ink: #2b2b2b;
    --paper: #fbfbfb;
    --rule: #d6d6d6;
    --backdrop: #d9d9d9;
    --soft-grey: #e4e4e4;
  }
  * { box-sizing: border-box; margin: 0; padding: 0; }
  html, body {
    width: 1200px; height: 786px; overflow: hidden;
    background: var(--backdrop);
    font-family: "Arimo", Arial, sans-serif;
  }
  .sheet {
    width: 1200px; height: 786px;
    display: flex; align-items: center; justify-content: center; gap: 40px;
  }
  .card {
    position: relative;
    width: 540px; height: 308px;
    border-radius: 18px;
    overflow: hidden;
    box-shadow: 0 8px 24px rgba(0,0,0,0.18);
  }
  .card--front { background: var(--paper); }
  .card--back { background: var(--black); display: flex; align-items: center; justify-content: center; }

  .swoosh { position: absolute; inset: 0; width: 100%; height: 100%; }

  .brand {
    position: absolute; left: 30px; top: 104px;
    width: 270px;
    font-weight: 300; font-size: 20px; letter-spacing: 1px;
    text-transform: uppercase; color: var(--orange);
    white-space: nowrap;
    display: flex; align-items: center; gap: 8px;
  }
  .brand__dot { width: 8px; height: 8px; border-radius: 50%; background: var(--orange); flex: none; }

  .divider {
    position: absolute; left: 318px; top: 70px;
    width: 1px; height: 150px; background: var(--rule);
  }

  .contact {
    position: absolute; left: 336px; top: 82px;
    color: var(--ink); font-size: 12.5px; line-height: 1.45;
    white-space: nowrap;
  }
  .contact__name {
    color: var(--orange); font-weight: 700; font-size: 15px;
    text-transform: uppercase; letter-spacing: 0.3px;
  }
  .contact__role { margin-bottom: 12px; }
  .contact__lines { margin-bottom: 12px; }

  .back-brand {
    font-weight: 300; font-size: 36px; letter-spacing: 1.5px;
    text-transform: uppercase; color: var(--orange);
  }
</style>
</head>
<body>
<main class="sheet">
  <section class="card card--front" aria-label="Business card front">
    <svg class="swoosh" viewBox="0 0 540 308" preserveAspectRatio="none" aria-hidden="true">
      <path d="M0,170 C110,190 190,240 235,308 L0,308 Z" fill="var(--black)"/>
      <path d="M0,162 C112,182 196,236 244,308" fill="none" stroke="var(--soft-grey)" stroke-width="8"/>
      <path d="M0,170 C110,190 190,240 235,308" fill="none" stroke="var(--orange)" stroke-width="6"/>
    </svg>

    <div class="brand"><span class="brand__dot"></span>Tallowind Shield</div>
    <div class="divider"></div>

    <div class="contact">
      <p class="contact__name">Morgan Telford</p>
      <p class="contact__role">General Manager</p>
      <div class="contact__lines">
        <p>02 9461 2738</p>
        <p>sales@tallowindshield.com.au</p>
        <p>www.tallowindshield.com.au</p>
      </div>
      <p>Unit 14, 172 Garrick Road</p>
      <p>Wexley Vale, NSW 2381</p>
    </div>
  </section>

  <section class="card card--back" aria-label="Business card back">
    <p class="back-brand">Tallowind Shield</p>
  </section>
</main>
</body>
</html>
```